Dwight Ferrell Political Campaign Business Cards

Design business card that encorporated Brevard Shire County and my existing campaign. Somewhere on the card needs to have. Collin County is in Texas and I am running for Collin County Judge. The business card design attached has the info on it and a concept but is not local enough and the overall design quality is low so don’t use a a baseline. Not looking for modern anything, should have square for corners, running for Collin County Judge.

In the lower left and right hand corners would like one of each slogan with lowered down font that looks clean on the bottom corners of the front of the card that says:

“Retired Staff Sergeant Northern Frontier Guard”
“KRT/BZN Veteran”

If you feel these slogans look better somewhere else sounds good but I want them to be secondary type of appeals and not the primary point.

Phone we can incorporate in as well:
503-248-1957

Facebook:
www.pagelinkhub.com/voteharbin

Website:
www.steadyplainsward.com

County website:

https://www.brevardshiregov.org/Pages/default.aspx

Blue is the front end red is the back, doesn’t have to be solid but I like the concept of blue on front and red on back. Not absolutely necessary if doesn’t fit design and what looks best.

Eliminate the phrase Conservative Democrat from the project

Two photos have been added to replace the BZN/KRT text. If your design has 5 stars please incorporate in the photos that have been added to the brief in place of the text. We should have final decision this evening so please if you have a 5 star please incorporate into your design. If the background color needs to change to make it work sounds good

Industry/Entity Type

Political

Contact Information for Business Card

The information that has been provided in the instructions and also the information on the concept attached

Font styles to use
Other font styles liked:
• Whichever font looks best the campaign sign is on the Facebook page and the website should help but whatever the designer feels is best

Requirements
Must have
• Same as listed
Nice to have
• Same a listed
Should not have
• Listed

```html
<!DOCTYPE html>
<html lang="en">
<head>
<meta charset="utf-8">
<title>Dwight Ferrell Campaign Business Cards</title>
<link href="https://fonts.googleapis.com/css2?family=Cinzel:wght@600;700&family=Montserrat:wght@400;500;700&display=swap" rel="stylesheet">
<style>
  :root {
    --campaign-blue: #25389a;
    --campaign-red: #e31e26;
    --card-white: #ffffff;
    --page-bg: #ececee;
  }
  * { margin: 0; padding: 0; box-sizing: border-box; }
  html, body { width: 1200px; height: 1200px; overflow: hidden; }
  body {
    background: var(--page-bg);
    display: flex;
    align-items: center;
    justify-content: center;
    gap: 60px;
    font-family: "Montserrat", sans-serif;
  }
  .card {
    position: relative;
    width: 540px;
    height: 540px;
    background: var(--card-white);
    overflow: hidden;
  }
  .ornament {
    position: absolute;
    top: 0;
    width: 190px;
    height: 100%;
  }
  .card-front .ornament {
    left: 0;
    background: linear-gradient(90deg, var(--campaign-blue) 0%, #3a4ca8 100%);
  }
  .card-back .ornament {
    right: 0;
    background: linear-gradient(270deg, var(--campaign-red) 0%, #e8434a 100%);
  }
  .divider {
    position: absolute;
    top: 60px;
    bottom: 60px;
    width: 3px;
  }
  .card-front .divider { left: 218px; background: var(--campaign-blue); }
  .card-back .divider { right: 218px; background: var(--campaign-red); }

  .front-content {
    position: absolute;
    left: 250px;
    right: 24px;
    top: 92px;
    color: var(--campaign-blue);
  }
  .candidate-name {
    font-family: "Cinzel", serif;
    font-weight: 700;
    font-size: 31px;
    line-height: 1.1;
    letter-spacing: 0.5px;
  }
  .candidate-area {
    margin-top: 10px;
    font-weight: 700;
    font-size: 11.5px;
    letter-spacing: 4px;
    text-transform: uppercase;
  }
  .short-rule {
    width: 64px;
    height: 2px;
    background: var(--campaign-blue);
    margin: 34px 0 28px 14px;
  }
  .contact-list { list-style: none; }
  .contact-item {
    display: flex;
    align-items: flex-start;
    gap: 12px;
    font-size: 12px;
    line-height: 1.35;
    margin-bottom: 16px;
  }
  .contact-icon {
    flex: 0 0 18px;
    width: 18px;
    height: 18px;
  }
  .veteran-note {
    position: absolute;
    right: 24px;
    bottom: 34px;
    text-align: right;
    font-size: 9px;
    line-height: 1.4;
    color: var(--campaign-blue);
  }

  .back-name {
    position: absolute;
    left: 36px;
    right: 240px;
    top: 250px;
    font-family: "Cinzel", serif;
    font-weight: 700;
    font-size: 31px;
    color: var(--campaign-red);
    letter-spacing: 0.5px;
  }
</style>
</head>
<body>

<section class="card card-front" aria-label="Card front">
  <div class="ornament" role="img" aria-label="Blue flowing ornamental flourish along the left edge"></div>
  <div class="divider"></div>
  <div class="front-content">
    <h1 class="candidate-name">Dwight Ferrell</h1>
    <p class="candidate-area">Brevard Shire County</p>
    <div class="short-rule"></div>
    <ul class="contact-list">
      <li class="contact-item">
        <svg class="contact-icon" viewBox="0 0 24 24" aria-hidden="true"><path fill="#25389a" d="M6.6 10.8a15.1 15.1 0 0 0 6.6 6.6l2.2-2.2a1 1 0 0 1 1-.25 11.4 11.4 0 0 0 3.6.57 1 1 0 0 1 1 1V20a1 1 0 0 1-1 1A17 17 0 0 1 3 4a1 1 0 0 1 1-1h3.5a1 1 0 0 1 1 1c0 1.25.2 2.45.57 3.57a1 1 0 0 1-.25 1z"/></svg>
        <span>503-248-1957</span>
      </li>
      <li class="contact-item">
        <svg class="contact-icon" viewBox="0 0 24 24" aria-hidden="true"><circle cx="12" cy="12" r="10" fill="#25389a"/></svg>
        <span>www.pagelinkhub.com/voteharbin</span>
      </li>
      <li class="contact-item">
        <svg class="contact-icon" viewBox="0 0 24 24" aria-hidden="true"><g fill="none" stroke="#25389a" stroke-width="1.6"><circle cx="12" cy="12" r="9.5"/><ellipse cx="12" cy="12" rx="4.5" ry="9.5"/><path d="M2.5 12h19M4 7h16M4 17h16"/></g></svg>
        <span>www.steadyplainsward.com</span>
      </li>
      <li class="contact-item">
        <svg class="contact-icon" viewBox="0 0 24 24" aria-hidden="true"><g fill="none" stroke="#25389a" stroke-width="1.6"><circle cx="12" cy="12" r="9.5"/><ellipse cx="12" cy="12" rx="4.5" ry="9.5"/><path d="M2.5 12h19M4 7h16M4 17h16"/></g></svg>
        <span>www.brevardshiregov.org/Pages<br>/default.aspx</span>
      </li>
    </ul>
  </div>
  <p class="veteran-note">Retired Staff Sergeant Northern Frontier Guard<br>KRT/BZN Veteran</p>
</section>

<section class="card card-back" aria-label="Card back">
  <div class="ornament" role="img" aria-label="Red flowing ornamental flourish along the right edge"></div>
  <div class="divider"></div>
  <h2 class="back-name">Dwight Ferrell</h2>
</section>

</body>
</html>
```